TovaLamarpe - Israeli Mental Health Website

We are developing an Israeli website for mental health. The website will be both in English and in Hebrew. We have a logo and would like a website design based on the logo and the logos colors (attached).

Attached is a doc that contains the website requirements.

We would like to have an icon for each of the sidebar categories, an image for each of the pages (including each of the sidebar category pages).

Target Market(s)

Adults 18-80

Industry/Entity Type

Mental Health

Number of Pages Required

5+ page

Font styles to use
Sans Serif

Colors

Designer to choose colors to be used in the design.

```html
<!DOCTYPE html>
<html lang="en">
<head>
<meta charset="utf-8">
<title>TovaLamarpe</title>
<link href="https://fonts.googleapis.com/css2?family=Archivo:wght@600;700;800&family=Nunito+Sans:wght@400;600;700&display=swap" rel="stylesheet">
<style>
:root{
  --blue:#2277c0;
  --green:#52ad43;
  --ink:#1d1d1d;
  --white:#ffffff;
  --black:#000000;
  --head:"Archivo",Arial,sans-serif;
  --body:"Nunito Sans",Arial,sans-serif;
}
*{margin:0;padding:0;box-sizing:border-box}
html,body{width:1200px;height:2279px;overflow:hidden;background:var(--white)}
body{position:relative;font-family:var(--body);color:var(--ink)}
.abs{position:absolute}
.pill{position:absolute;border-radius:999px;display:flex;align-items:center;justify-content:center;font-family:var(--head);font-weight:700;color:var(--white);text-transform:uppercase}

.topbar{left:0;top:0;width:1200px;height:35px;background:var(--blue)}
.topbar-text{left:654px;top:11px;font-family:var(--head);font-weight:700;font-size:11px;color:var(--white);word-spacing:2px}
.social-dot{width:17px;height:17px;border-radius:50%;background:var(--white);top:9px}
.btn-contact{left:995px;top:4px;width:91px;height:27px;background:var(--green);font-size:11px}

.nav{left:0;top:35px;width:1200px;height:69px;background:var(--white)}
.brand{left:120px;top:50px;display:flex;align-items:center;gap:8px;font-family:var(--body);font-weight:700;font-size:17px;color:var(--blue)}
.brand-dot{width:28px;height:28px;border-radius:50%;background:var(--blue)}
.nav-link{top:62px;font-size:16px;color:var(--ink)}
.btn-donate{left:994px;top:55px;width:92px;height:29px;background:var(--green);font-size:11px}

.hero{left:0;top:104px;width:1200px;height:525px;background:linear-gradient(100deg,#6b5552 0%,#8a7a78 35%,#b7aaa5 60%,#d9d0cc 80%,#9d9391 100%)}
.hero-title{left:112px;top:256px;font-family:var(--head);font-weight:800;font-size:46px;color:var(--white)}
.hero-copy{left:114px;top:324px;width:480px;font-size:11.6px;line-height:15px;letter-spacing:-0.1px;color:var(--white)}
.btn-heal{left:115px;top:394px;width:250px;height:44px;background:var(--green);font-size:15px}

.emergency{left:122px;top:566px;width:956px;height:272px;background:var(--blue);text-align:center;color:var(--white)}
.emergency h2{margin-top:40px;font-family:var(--head);font-weight:800;font-size:30px}
.emergency p{margin:12px auto 0;width:775px;font-size:15.5px;line-height:19px}

.card{width:387px;height:287px;background:var(--white);box-shadow:0 0 24px rgba(0,0,0,.10);text-align:center}
.card-photo{display:block;width:139px;height:139px;border-radius:50%;margin:22px auto 0}
.card h3{margin-top:17px;font-family:var(--head);font-weight:700;font-size:18px;color:var(--blue)}
.card p{margin:10px auto 0;width:355px;font-size:11.8px;line-height:19px;letter-spacing:-0.1px}

.about{left:0;top:1398px;width:1200px;height:347px;background:var(--green)}
.about-photo{left:220px;top:1445px;width:268px;height:268px;border-radius:50%;background:linear-gradient(160deg,#f1efec,#cfc6bc 55%,#8f8472)}
.about-title{left:590px;top:1476px;font-family:var(--head);font-weight:800;font-size:30px;color:var(--white)}
.about-copy{left:591px;top:1521px;width:492px;font-size:11.7px;line-height:18.7px;letter-spacing:-0.1px;color:var(--white)}
.btn-learn{left:590px;top:1635px;width:145px;height:42px;background:var(--blue);font-size:12px}

.news-title{left:0;top:1785px;width:1200px;text-align:center;font-family:var(--head);font-weight:800;font-size:30px;color:var(--blue)}
.news-copy{left:205px;top:1834px;width:790px;text-align:center;font-size:12px;line-height:19px;letter-spacing:-0.1px}
.news-field{left:347px;top:1901px;width:425px;height:43px;border-radius:22px;background:var(--white);box-shadow:0 0 12px rgba(0,0,0,.10)}
.news-field span{position:absolute;left:20px;top:13px;font-size:12px}
.news-go{left:714px;top:1907px;width:51px;height:31px;border-radius:16px;background:var(--green)}

.footer{left:0;top:1985px;width:1200px;height:294px;background:var(--black);color:var(--white)}
.foot-brand{left:121px;top:2050px;display:flex;align-items:center;gap:8px;font-weight:700;font-size:24px;color:var(--white)}
.foot-brand-dot{width:34px;height:34px;border-radius:50%;background:var(--white)}
.foot-about{left:122px;top:2111px;width:168px;font-size:11.5px;line-height:19px;color:var(--white)}
.foot-head{top:2047px;font-family:var(--head);font-weight:800;font-size:18px;color:var(--white)}
.foot-link{left:427px;font-size:15px;color:var(--white)}
.foot-social{left:655px;display:flex;align-items:center;gap:9px;font-size:15px;color:var(--white)}
.foot-social i{width:17px;height:17px;border-radius:50%;background:var(--white);display:block}
.foot-input{left:887px;width:199px;height:35px;border-radius:18px;background:var(--white);color:var(--ink);font-size:11.5px;padding:11px 12px}
.btn-submit{left:891px;top:2177px;width:104px;height:37px;background:var(--green);color:var(--black);font-size:14px;font-weight:800}
.copyright{left:122px;top:2233px;font-size:11.5px;color:var(--white)}
</style>
</head>
<body>

<div class="abs topbar"></div>
<div class="abs topbar-text">+123 456 7890 &nbsp;Request Appointmemt</div>
<div class="abs social-dot" style="left:880px"></div>
<div class="abs social-dot" style="left:918px"></div>
<div class="abs social-dot" style="left:958px"></div>
<div class="pill btn-contact">Contact</div>

<div class="abs nav"></div>
<div class="abs brand"><span class="brand-dot"></span>TovaLamarpe</div>
<div class="abs nav-link" style="left:476px">Therapists</div>
<div class="abs nav-link" style="left:586px">Organizations</div>
<div class="abs nav-link" style="left:716px">Videos</div>
<div class="abs nav-link" style="left:799px">Contact</div>
<div class="abs nav-link" style="left:895px">About</div>
<div class="pill btn-donate">Donate</div>

<div class="abs hero" role="img" aria-label="Photo of a thoughtful young woman in a soft sweater gazing out of a window"></div>
<h1 class="abs hero-title">YOU ARE NOT ALONE.</h1>
<p class="abs hero-copy">Lorem Ipsum is simply dummy text of the printing and typesetting industry. Lorem Ipsum has been the industry's standard dummy text ever since the 1500s, when an unknown printer took a galley of type and scrambled it to make a type specimen book. It has</p>
<div class="pill btn-heal">Start your healing today</div>

<section class="abs emergency">
  <h2>EMERGENCY MENTAL HELP</h2>
  <p>Lorem ipsum dolor sit amet, consectetur adipiscing elit, sed do eiusmod tempor incididunt ut labore et dolore magna aliqua. Ut enim ad minim veniam, quis nostrud exercitation ullamco laboris nisi ut aliquip ex ea commodo consequat.</p>
</section>

<article class="abs card" style="left:203px;top:750px">
  <span class="card-photo" role="img" aria-label="Photo of two people holding hands in support" style="background:linear-gradient(150deg,#d9d2cb,#b08d72 55%,#4d4845)"></span>
  <h3>Therapists</h3>
  <p>Lorem ipsum dolor sit amet, consectetur adipiscing elit, sed do eiusmod tempor incididunt ut labore et dolore magna aliqua. Ut enim ad minim veniam, quis nostrud exercitation ullamco laboris</p>
</article>
<article class="abs card" style="left:609px;top:750px">
  <span class="card-photo" role="img" aria-label="Photo of a pensive woman holding a mug by a window" style="background:linear-gradient(150deg,#d8d4cf,#8b7a6c 50%,#3e3632)"></span>
  <h3>Grief &amp; loss</h3>
  <p>Lorem ipsum dolor sit amet, consectetur adipiscing elit, sed do eiusmod tempor incididunt ut labore et dolore magna aliqua. Ut enim ad minim veniam, quis nostrud exercitation ullamco laboris</p>
</article>
<article class="abs card" style="left:203px;top:1062px">
  <span class="card-photo" role="img" aria-label="Photo of a stressed woman sitting with her head in her hands" style="background:linear-gradient(150deg,#e4e4e4,#a7a7a7 55%,#5d5d5d)"></span>
  <h3>Stress management</h3>
  <p>Lorem ipsum dolor sit amet, consectetur adipiscing elit, sed do eiusmod tempor incididunt ut labore et dolore magna aliqua. Ut enim ad minim veniam, quis nostrud exercitation ullamco laboris</p>
</article>
<article class="abs card" style="left:609px;top:1062px">
  <span class="card-photo" role="img" aria-label="Photo of a woman comforting a friend on a sofa" style="background:linear-gradient(150deg,#f2f0ee,#d0c4b8 50%,#3f4c68)"></span>
  <h3>Infidelity &amp; betrayal</h3>
  <p>Lorem ipsum dolor sit amet, consectetur adipiscing elit, sed do eiusmod tempor incididunt ut labore et dolore magna aliqua. Ut enim ad minim veniam, quis nostrud exercitation ullamco laboris</p>
</article>

<section class="abs about"></section>
<div class="abs about-photo" role="img" aria-label="Photo of a support group of three women comforting each other"></div>
<h2 class="abs about-title">ABOUT US</h2>
<p class="abs about-copy">Lorem ipsum dolor sit amet, consectetur adipiscing elit, sed do eiusmod tempor incididunt ut labore et dolore magna aliqua. Ut enim ad minim veniam, quis nostrud exercitation ullamco laboris nisi ut aliquip ex ea commodo consequat. Duis aute irure dolor in reprehenderit in voluptate velit esse cillum dolore eu fugiat nulla pariatur. Excepteur sint occaecat cupidatat non proident, sunt in culpa qui officia deserunt mollit anim id est laborum</p>
<div class="pill btn-learn">Learn more</div>

<h2 class="abs news-title">SING UP FOR OUR NEWSLETTER</h2>
<p class="abs news-copy">Lorem Ipsum is simply dummy text of the printing and typesetting industry. Lorem Ipsum has been the industry's standard dummy text ever since the 1500s, when an unknown printer took a galley of type and scrambled it to make a type specimen book.</p>
<div class="abs news-field"><span>Enter your email address</span></div>
<div class="abs news-go">
  <svg width="51" height="31" viewBox="0 0 51 31"><path d="M17 15.5h17M29 10.5l5 5-5 5" fill="none" stroke="#fff" stroke-width="1.8" stroke-linecap="round" stroke-linejoin="round"/></svg>
</div>

<footer class="abs footer"></footer>
<div class="abs foot-brand"><span class="foot-brand-dot"></span>TovaLamarpe</div>
<p class="abs foot-about">Lorem Ipsum is simply dummy text of the printing and typesetting industry. Lorem Ipsum has been the industry's standard dummy text ever</p>

<div class="abs foot-head" style="left:427px">MENU</div>
<div class="abs foot-link" style="top:2079px">Therapists</div>
<div class="abs foot-link" style="top:2109px">Organizations</div>
<div class="abs foot-link" style="top:2139px">Videos</div>
<div class="abs foot-link" style="top:2169px">Contact</div>
<div class="abs foot-link" style="top:2199px">About</div>

<div class="abs foot-head" style="left:655px">FOLLOW US</div>
<div class="abs foot-social" style="top:2083px"><i></i>HEARTLINK</div>
<div class="abs foot-social" style="top:2128px"><i></i>PROFILENET</div>
<div class="abs foot-social" style="top:2175px"><i></i>SNAPSHARE</div>

<div class="abs foot-head" style="left:884px">CONTACT</div>
<div class="abs foot-input" style="top:2088px">NAME</div>
<div class="abs foot-input" style="top:2132px">EMAIL</div>
<div class="pill btn-submit">Submit</div>

<div class="abs copyright">Copyright © 2023 Quiet Harbor. All rights reserved.</div>

</body>
</html>
```